Newsletter Ad

I am looking for someone to design an advertisement for a mother's club newsletter. 4" wide X by 5" tall (and 2.5" wide X 5" tall if possible).

I'm a psychotherapist, so want the ad to look professional, but modern. I have a logo with my photo attached that can be incorporated into the design. The colors of my website are turquoise and white. I'd like to keep with that theme...so maybe some turquoise blocking to match the logo font color.

I'm uploading a logo as well as an ad draft with the content I'd like listed in the ad.

```html
<!DOCTYPE html>
<html lang="en">
<head>
<meta charset="utf-8">
<title>Dana Morel, MA, MFT – Newsletter Ads</title>
<link rel="stylesheet" href="https://fonts.googleapis.com/css2?family=Archivo+Black&family=Arimo:wght@400;700&display=swap">
<style>
  :root {
    --stage: #e4f3f4;
    --card-top: #ffffff;
    --card-mid: #c9f3f3;
    --card-bottom: #2fdadc;
    --turquoise: #3fd6d6;
    --turquoise-deep: #1fb8bb;
    --ink: #111111;
    --paper: #ffffff;
    --photo-a: #6b5a4c;
    --photo-b: #1c1a1a;
    --ornament: #b9d7d8;
  }
  * { margin: 0; padding: 0; box-sizing: border-box; }
  html, body { width: 1200px; height: 900px; overflow: hidden; }
  body { position: relative; background: var(--stage); font-family: "Arimo", Arial, sans-serif; }

  .ad {
    position: absolute;
    overflow: hidden;
    background: linear-gradient(180deg, var(--card-top) 0%, var(--card-mid) 35%, var(--card-bottom) 100%);
    text-align: center;
    color: var(--ink);
  }
  .ad--narrow { left: 48px; top: 38px; width: 360px; height: 722px; }
  .ad--wide   { left: 478px; top: 15px; width: 637px; height: 795px; }

  .portrait {
    position: absolute; left: 0; top: 0;
    background: linear-gradient(160deg, var(--photo-a), var(--photo-b));
  }
  .ad--narrow .portrait { width: 87px; height: 132px; }
  .ad--wide .portrait { width: 148px; height: 223px; }

  .masthead { position: absolute; }
  .ad--narrow .masthead { left: 98px; top: 45px; width: 255px; }
  .ad--wide .masthead { left: 165px; top: 66px; width: 445px; }

  .rule { height: 3px; background: var(--turquoise); }
  .ad--narrow .rule--top { width: 175px; margin-bottom: 4px; }
  .ad--narrow .rule--bottom { width: 175px; margin: 3px 0 0 auto; }
  .ad--wide .rule--top { width: 302px; margin-bottom: 6px; }
  .ad--wide .rule--bottom { width: 302px; margin: 6px 0 0 auto; }

  .name {
    font-family: "Arimo", Arial, sans-serif; font-weight: 400;
    color: var(--turquoise);
    text-shadow: 1px 1px 0 var(--turquoise-deep), 2px 3px 3px rgba(0,0,0,.45);
    white-space: nowrap;
    text-align: left;
    letter-spacing: -0.5px;
    line-height: 1.1;
  }
  .ad--narrow .name { font-size: 21.5px; }
  .ad--wide .name { font-size: 38px; }

  .tagline {
    position: absolute; font-family: "Archivo Black", sans-serif;
    text-transform: uppercase; line-height: 1.1;
    text-shadow: 1px 1px 1px rgba(0,0,0,.3);
  }
  .ad--narrow .tagline { left: 100px; top: 108px; width: 240px; font-size: 10px; }
  .ad--wide .tagline { left: 205px; top: 185px; width: 370px; font-size: 16px; letter-spacing: .5px; }

  .specialties { list-style: none; font-family: "Archivo Black", sans-serif; position: absolute; }
  .specialties li { color: var(--ink); text-shadow: 1px 2px 2px rgba(0,0,0,.35); letter-spacing: .8px; white-space: nowrap; }
  .specialties .accent { color: var(--turquoise-deep); }

  .ad--narrow .specialties { left: 0; top: 215px; width: 360px; font-size: 15px; line-height: 32.6px; }

  .ad--wide .specialties { left: 0; top: 0; width: 637px; height: 100%; font-size: 25px; }
  .ad--wide .specialties li { position: absolute; }

  .contact {
    position: absolute; left: 0; width: 100%;
    font-style: normal; font-family: "Archivo Black", sans-serif;
    color: var(--paper); text-shadow: 1px 1px 2px rgba(0,0,0,.55);
    white-space: nowrap;
  }
  .ad--narrow .contact { top: 584px; font-size: 13px; line-height: 19px; }
  .ad--wide .contact { top: 580px; font-size: 23.5px; line-height: 31px; letter-spacing: .5px; }
  .contact .web { color: #eafafa; }

  .license { position: absolute; left: 0; width: 100%; font-family: "Archivo Black", sans-serif; text-shadow: 1px 1px 2px rgba(0,0,0,.3); }
  .ad--narrow .license { top: 684px; font-size: 14px; }
  .ad--wide .license { top: 752px; font-size: 26px; letter-spacing: 1px; }

  .ornament { position: absolute; background: var(--ornament); opacity: .55; border-radius: 6px; }
  .ornament--left { left: 0; top: 620px; width: 92px; height: 168px; }
  .ornament--right { right: 0; top: 620px; width: 92px; height: 168px; }
</style>
</head>
<body>

  <section class="ad ad--narrow" aria-label="2.5 by 5 inch ad">
    <div class="portrait" role="img" aria-label="Portrait photo of the therapist"></div>
    <header class="masthead">
      <div class="rule rule--top"></div>
      <h1 class="name">DANA MOREL, MA, MFT</h1>
      <div class="rule rule--bottom"></div>
    </header>
    <p class="tagline">Psychotherapy for individuals,<br>couples and families</p>
    <ul class="specialties">
      <li><span class="accent">* Parenting</span></li>
      <li>*Depression</li>
      <li>* Anxiety</li>
      <li>* Divorce</li>
      <li><span class="accent">* Life Transitions</span></li>
      <li>* Couples Issues</li>
      <li><span class="accent">* Women's Issues</span></li>
      <li>* Attachment and Neuroscience</li>
    </ul>
    <address class="contact">
      148 Harbor Lane, Bay Hollow, CA 94000<br>
      <span class="web">www.danamorel.com</span><br>
      dana@danamorel.com<br>
      555.014.2290
    </address>
    <p class="license">License# MFC48120</p>
  </section>

  <section class="ad ad--wide" aria-label="4 by 5 inch ad">
    <div class="portrait" role="img" aria-label="Portrait photo of the therapist"></div>
    <header class="masthead">
      <div class="rule rule--top"></div>
      <h1 class="name">DANA MOREL, MA, MFT</h1>
      <div class="rule rule--bottom"></div>
    </header>
    <p class="tagline">Psychotherapy for individuals,<br>couples and families</p>
    <ul class="specialties">
      <li style="left:27px;top:282px">* Parenting</li>
      <li style="left:420px;top:282px">*Depression</li>
      <li style="left:27px;top:349px">* Divorce</li>
      <li style="left:185px;top:349px"><span class="accent">* Life Transitions</span></li>
      <li style="left:458px;top:349px">* Anxiety</li>
      <li style="left:27px;top:416px"><span class="accent">* Women's Issues</span></li>
      <li style="left:360px;top:416px">* Couples Issues</li>
      <li style="left:90px;top:478px">* Attachment and Neuroscience</li>
    </ul>
    <div class="ornament ornament--left" role="img" aria-label="Decorative scroll ornament"></div>
    <div class="ornament ornament--right" role="img" aria-label="Decorative scroll ornament"></div>
    <address class="contact">
      148 Harbor Lane, Bay Hollow, CA 94000<br>
      <span class="web">www.danamorel.com</span><br>
      dana@danamorel.com<br>
      555.014.2290
    </address>
    <p class="license">License# MFC48120</p>
  </section>

</body>
</html>
```